High-end dermatology office brochure design

Corvella Skin and Laser is a high-end dermatology practice that specializes in custom skin care solutions, and skin cancer surveillance and treatment. Brochure should be elegant, but informative to attract high-end customers.

Target Market(s)

Men and women 27-60

Industry/Entity Type

Office

Requirements
Must have
• Attached document has required copy, including, websites, address and company phone number
Nice to have
• images

```html
<!DOCTYPE html>
<html lang="en">
<head>
<meta charset="utf-8">
<title>Corvella Skin and Laser – Services</title>
<link rel="stylesheet" href="https://fonts.googleapis.com/css2?family=Libre+Baskerville:wght@700&family=Cabin:wght@400&display=swap">
<style>
  :root {
    --sage: #e0e5b2;
    --plum: #714482;
    --plum-text: #6d4380;
    --cream: #dcdfa2;
    --ink: #1b1b1b;
    --white: #ffffff;
    --ornament-fill: #8a6399;
  }
  * { margin: 0; padding: 0; box-sizing: border-box; }
  html, body { width: 1200px; height: 927px; overflow: hidden; }
  body { font-family: "Cabin", sans-serif; font-size: 16.5px; line-height: 20.8px; }
  .brochure { position: relative; width: 1200px; height: 927px; }
  .panel { position: absolute; top: 0; height: 927px; }
  .panel--medical { left: 0; width: 600px; background: var(--sage); color: var(--ink); }
  .panel--cosmetic { left: 600px; width: 600px; background: var(--plum); color: var(--white); }
  .block { position: absolute; }
  .panel--medical .block { left: 82px; width: 490px; }
  .panel--cosmetic .block { left: 82px; width: 500px; }
  .section-title {
    position: absolute; left: 28px;
    font-family: "Libre Baskerville", serif; font-weight: 700;
    font-size: 23px; letter-spacing: -0.3px;
  }
  .panel--medical .section-title { color: var(--plum-text); }
  .panel--cosmetic .section-title { color: var(--cream); }
  .sub-title { position: absolute; left: 28px; font-size: 18px; }
  .panel--medical .sub-title { color: var(--plum-text); }
  .panel--cosmetic .sub-title { color: var(--cream); }
  .service-list { position: absolute; list-style: none; }
  .panel--medical .service-list { left: 138px; color: var(--plum-text); font-size: 17px; line-height: 20.5px; }
  .panel--cosmetic .service-list { left: 136px; color: var(--cream); font-size: 17px; line-height: 21px; }
  .service-list li { position: relative; padding-left: 26px; }
  .panel--cosmetic .service-list li { padding-left: 55px; }
  .service-list li::before {
    content: ""; position: absolute; left: 1px; top: 7px;
    width: 12px; height: 7px;
    border: 2px solid currentColor; border-top-color: transparent;
    border-radius: 0 0 8px 8px;
  }
  .service-list .note { display: block; }
  .ornament-row { position: absolute; top: 740px; left: 32px; display: flex; gap: 30px; }
  .ornament-tile { width: 160px; height: 160px; background: var(--ornament-fill); border-radius: 4px; }
</style>
</head>
<body>
<main class="brochure">
  <section class="panel panel--medical">
    <h2 class="section-title" style="top:24px">Medical services</h2>
    <p class="block" style="top:70px">We’re leaders in the diagnosis of all skin conditions and autoimmune skin conditions, including:</p>
    <ul class="service-list" style="top:132px">
      <li>rashes</li><li>acne</li><li>warts</li><li>skin tags</li><li>rosacea</li><li>psoriasis</li>
    </ul>
    <p class="block" style="top:275px">We’re also involved in ongoing research for the treatment of psoriasis.</p>
    <h3 class="sub-title" style="top:334px">Skin cancer surveillance and treatment</h3>
    <p class="block" style="top:377px">Skin cancer can form anywhere on the skin (even where the sun doesn’t shine), so it’s vital that a full body exam is done at least once a year.</p>
    <p class="block" style="top:459px">We pride ourselves on thorough surveillance and commitment to your overall health.</p>
    <h3 class="sub-title" style="top:518px">Alternative care</h3>
    <p class="block" style="top:561px">Your commitment to your health is the same as our commitment to you. We provide non-antibiotic acne treatment including botanicals, blue light and a combination of supplements to fit your personal lifestyle.</p>
    <h2 class="section-title" style="top:682px">Dermatologic surgery services</h2>
    <p class="block" style="top:732px">We have in-house surgeons for the removal of atypical moles and skin cancers, including margin control for melanoma. Our board-certified, in-house surgeons specialize in:</p>
    <ul class="service-list" style="top:816px">
      <li>Plastic surgery</li>
      <li>Mohs surgery<span class="note">(treatment includes transportation and<br>care from your trusted healthcare team)</span></li>
    </ul>
  </section>

  <section class="panel panel--cosmetic">
    <h2 class="section-title" style="top:24px">Cosmetic services</h2>
    <p class="block" style="top:82px">Your skin is unique, so we take pride in our ability to provide personalized consultations and skin care analysis to set you up with the right treatments and products.</p>
    <ul class="service-list" style="top:167px">
      <li>Chemical peels</li><li>Photofacial</li><li>Ultralift</li><li>Lumina</li><li>IPL</li>
      <li>Injectables and fillers<span class="note" style="margin-left:0">(Revelane, Velvederm, Bellasoft, Neurosmooth and Relaxa)</span></li>
    </ul>
    <h3 class="sub-title" style="top:334px">Elite-grade cosmeceutical products</h3>
    <p class="block" style="top:380px">Including Verdane, June Marlow, Imprint, Tintlab, Skin Notes, Lashera and much more.</p>
    <h3 class="sub-title" style="top:443px">Aesthetic services</h3>
    <p class="block" style="top:490px">Facials, peels, microdermabrasion, body wraps, waxing, eyelash extensions, brow tinting</p>
    <h2 class="section-title" style="top:574px">Nutrition and supplement support</h2>
    <p class="block" style="top:632px">Including gluten free, no filler multi-vitamins, immune boosters, hormone, sleep aid balancing products, B12 injections and the Slim Shot.</p>
    <div class="ornament-row">
      <div class="ornament-tile" role="img" aria-label="Decorative rosette medallion in a framed tile"></div>
      <div class="ornament-tile" role="img" aria-label="Decorative rosette medallion in a framed tile"></div>
      <div class="ornament-tile" role="img" aria-label="Decorative rosette medallion in a framed tile"></div>
    </div>
  </section>
</main>
</body>
</html>
```